LKND - Ledgers Kept Neatly Daily

We need a business card design for a company located in Australia - accounting / tax firm.

2 sided business card - I have attached a one-sided concept that I did in MSWord :) If anything it shows that I want a striking design - bold, fresh and less reserved than your average accounting firm's card.

Rather than having all the info on the front, maybe it could just have name and logo on front?

Want to keep colours in line with logo - orange, black and white.

Happy for full colour. Will be using a matte finish.

About Us (below)
LKND does business, and more specifically accounting and taxation differently.
People require news and other media at their fingertips so why should business figures and documents be any different?
In combination with Quilo, a cloud based accounting package, we store all receipts, tax returns and special documentation with a secure online data-storage provider and provide you with your own login. We are also interested to hear if video conferencing is something you would be interested in.
Using this technology we are able to focus more on your business and less on the data entry.

Target Market(s)

Individual mum and dad clients, and Small to Medium Business

Industry/Entity Type

Accounting

Requirements
Must have
• Must be able to edit the details at a future point in time ie - phone, address, website address, name on card and slogan.

2 sided

Standard Australian business card size
Nice to have
• Rather than having all the info on the front, maybe it could just have name and logo on front?
Should not have
• Don't want "Ledgers Kept Neatly Daily" on the card

```html
<!DOCTYPE html>
<html lang="en">
<head>
<meta charset="utf-8">
<title>LKND business card</title>
<link rel="stylesheet" href="https://fonts.googleapis.com/css2?family=Source+Sans+3:wght@400;600;800&display=swap">
<style>
  :root {
    --bg: #e9e6e2;
    --orange-light: #f08a3e;
    --orange: #e2722a;
    --orange-deep: #c85a1a;
    --black: #1d1a18;
    --white: #ffffff;
    --mark: #f4b04a;
  }
  * { box-sizing: border-box; margin: 0; padding: 0; }
  html, body {
    width: 1200px; height: 1000px; overflow: hidden;
    background: var(--bg);
    font-family: "Source Sans 3", "Myriad Pro", Arial, sans-serif;
  }
  .sheet {
    width: 1200px; height: 1000px;
    display: flex; flex-direction: column; align-items: center; justify-content: center;
    gap: 40px;
  }
  .card {
    position: relative;
    width: 720px; height: 440px;
    background: linear-gradient(135deg, var(--orange-light) 0%, var(--orange) 55%, var(--orange-deep) 100%);
    overflow: hidden;
    box-shadow: 0 8px 24px rgba(0,0,0,.18);
    color: var(--white);
  }

  /* front */
  .card__tab {
    position: absolute; right: -22px; top: 70px;
    width: 60px; height: 90px;
    background: var(--black);
    border-radius: 18px;
  }
  .brand {
    position: absolute; left: 185px; top: 120px;
    display: flex; align-items: center; gap: 22px;
  }
  .brand__dot {
    width: 104px; height: 104px; border-radius: 50%;
    background: radial-gradient(circle at 40% 35%, var(--mark), var(--orange-deep));
  }
  .brand__text { display: flex; flex-direction: column; }
  .brand__name {
    font-size: 108px; font-weight: 400; line-height: .9; letter-spacing: 2px;
  }
  .brand__services {
    font-size: 16px; font-weight: 400; margin-top: 6px; letter-spacing: .2px;
  }
  .brand__services span { display: inline-block; width: 7px; height: 7px; border-radius: 50%; background: var(--white); margin: 0 5px 2px; vertical-align: middle; }
  .rule {
    position: absolute; left: 390px; right: 0; top: 292px;
    height: 2px; background: var(--white);
  }
  .person {
    position: absolute; left: 48px; top: 300px;
    display: flex; align-items: baseline; gap: 6px;
  }
  .person__name { font-size: 46px; font-weight: 800; letter-spacing: -1px; }
  .person__role { font-size: 20px; font-weight: 400; }

  /* back */
  .band {
    position: absolute; right: 0; top: 150px;
    width: 300px; height: 92px;
    background: var(--black);
  }
  .block {
    position: absolute; left: 0; top: 170px;
    width: 55px; height: 110px;
    background: var(--black);
  }
  .contact {
    position: absolute; left: 75px; top: 152px;
    list-style: none;
    font-size: 30px; line-height: 40px; font-weight: 400;
  }
  .contact li { display: flex; align-items: center; gap: 12px; }
  .contact svg { width: 30px; height: 30px; flex: none; }
</style>
</head>
<body>
<main class="sheet">

  <section class="card card--front" aria-label="Card front">
    <div class="card__tab"></div>
    <div class="brand">
      <div class="brand__dot"></div>
      <div class="brand__text">
        <div class="brand__name">LKND</div>
        <div class="brand__services">Bookkeeping<span></span>Accounting<span></span>Taxation</div>
      </div>
    </div>
    <div class="rule"></div>
    <div class="person">
      <span class="person__name">Martin Hale</span>
      <span class="person__role">Tax Agent</span>
    </div>
  </section>

  <section class="card card--back" aria-label="Card back">
    <div class="band"></div>
    <div class="block"></div>
    <ul class="contact">
      <li>
        <svg viewBox="0 0 30 30" aria-hidden="true"><rect x="2" y="7" width="26" height="17" fill="#fff"/><path d="M2 7 L15 17 L28 7" fill="none" stroke="#e2722a" stroke-width="2"/></svg>
        hale@lknd.com.au
      </li>
      <li>
        <svg viewBox="0 0 30 30" aria-hidden="true"><rect x="8" y="3" width="14" height="24" rx="3" fill="none" stroke="#fff" stroke-width="2"/><line x1="13" y1="23" x2="17" y2="23" stroke="#fff" stroke-width="2"/></svg>
        0412 555 018
      </li>
      <li>
        <svg viewBox="0 0 30 30" aria-hidden="true"><circle cx="15" cy="15" r="12" fill="#fff"/><ellipse cx="15" cy="15" rx="5" ry="12" fill="none" stroke="#e2722a" stroke-width="1.5"/><line x1="3" y1="15" x2="27" y2="15" stroke="#e2722a" stroke-width="1.5"/></svg>
        www.lknd.com.au
      </li>
    </ul>
  </section>

</main>
</body>
</html>
```